Flyer-Design für Gin-Unternehmen
Zielgruppe
Herstellung von GIN / GIN Liebhaber
Aufgabenstellung
Der Flyer soll unser Produkt ansprechend darstellen sowie uns als Familienbetrieb. Informationen Rund um unseren GIN und unser Projekt können Sie auf www.walbertsud.com beziehen.

```html
<!DOCTYPE html>
<html lang="de">
<head>
<meta charset="utf-8">
<title>Walbert Gin – Flyer DIN A5 quer</title>
<link rel="stylesheet" href="https://fonts.googleapis.com/css2?family=Raleway:ital,wght@0,400;0,500;0,600;0,700;0,800;1,400&display=swap">
<style>
  :root {
    --sheet: #efefef;
    --ink: #000000;
    --paper: #ffffff;
    --text: #1a1a1a;
    --shadow: #c9c9c9;
    --caption: #9fb4b6;
    --sky-top: #d9b59a;
    --sky-mid: #8fb0b2;
    --sky-low: #5d8585;
    --cellar-dark: #150d07;
    --cellar-warm: #7a4a1f;
    --cellar-glow: #c08a4a;
    --meadow: #7aa15c;
    --meadow-light: #c9d9b0;
    --yard: #a89c8a;
    --yard-light: #e3d6cf;
  }
  * { box-sizing: border-box; margin: 0; padding: 0; }
  html, body { width: 902px; height: 1200px; overflow: hidden; }
  body {
    background: var(--sheet);
    font-family: "Raleway", Arial, sans-serif;
    color: var(--text);
    position: relative;
  }
  .page {
    position: absolute;
    left: 82px;
    width: 760px;
    height: 535px;
    background: var(--ink);
    box-shadow: 7px 7px 0 var(--shadow);
    overflow: hidden;
  }
  .page--front { top: 48px; }
  .page--back { top: 606px; }

  .photo { position: absolute; }
  .front-photo {
    left: 0; top: 119px; width: 409px; height: 320px;
    background:
      radial-gradient(ellipse 55% 70% at 62% 62%, rgba(40,60,62,.55), transparent 70%),
      linear-gradient(180deg, var(--sky-top) 0%, var(--sky-mid) 28%, var(--sky-low) 100%);
  }
  .back-photo {
    left: 0; top: 0; width: 409px; height: 535px;
    background:
      radial-gradient(ellipse 40% 55% at 52% 62%, rgba(192,138,74,.55), transparent 70%),
      radial-gradient(ellipse 60% 40% at 30% 25%, rgba(122,74,31,.6), transparent 75%),
      linear-gradient(160deg, var(--cellar-warm) 0%, var(--cellar-dark) 55%, #2b1a0c 100%);
  }

  .hashtags {
    position: absolute; left: 40px; top: 176px;
    list-style: none; color: var(--paper);
    font-weight: 700; font-size: 17.5px; line-height: 33.7px;
  }

  .brand-wordmark {
    position: absolute; left: 400px; top: 18px;
    color: var(--paper);
    font-weight: 700; font-size: 118px; line-height: 1;
    letter-spacing: -2px; white-space: nowrap;
  }

  .text-panel {
    position: absolute; left: 358px; width: 402px;
    background: var(--paper);
  }
  .page--front .text-panel { top: 156px; height: 231px; }
  .page--back .text-panel { top: 138px; height: 330px; }

  .panel-copy {
    position: absolute; left: 29px; top: 18px;
    font-size: 10.4px; line-height: 18px; color: var(--text);
    white-space: nowrap;
  }
  .page--back .panel-copy { top: 17px; }
  .panel-copy b { font-weight: 700; }

  .panel-photo { left: 290px; width: 95px; }
  .grandfather-photo {
    top: 68px; height: 102px;
    background: linear-gradient(180deg, var(--meadow-light) 0%, var(--meadow) 55%, #4b5d3a 100%);
  }
  .founders-photo {
    top: 60px; height: 130px;
    background: linear-gradient(180deg, var(--yard) 0%, var(--yard-light) 60%, #d99fb0 100%);
  }

  .product-caption {
    position: absolute; left: 40px; top: 444px;
    color: var(--caption); font-size: 10.4px; font-weight: 500;
  }
  .label-note {
    position: absolute; left: 40px; top: 465px;
    color: var(--paper); font-size: 8.6px; line-height: 13.2px;
    white-space: nowrap;
  }
  .label-note b { font-weight: 700; }

  .web-address {
    position: absolute; left: 518px;
    color: var(--paper); font-weight: 700; font-size: 14.5px;
  }
  .page--front .web-address { top: 491px; }
  .page--back .web-address { top: 490px; }

  .headline {
    position: absolute; left: 257px; top: 34px;
    color: var(--paper); font-weight: 700; font-size: 17.5px; line-height: 33.7px;
  }

  .brand-signoff {
    position: absolute; left: 150px; top: 240px;
    color: var(--ink); font-weight: 700; font-size: 30px; line-height: 1;
    display: flex; align-items: center; gap: 8px;
  }
  .brand-signoff .dot { width: 9px; height: 9px; border-radius: 50%; background: var(--ink); }

  .contact-line {
    position: absolute; left: 423px; top: 516px;
    color: var(--paper); font-size: 7.4px; white-space: nowrap;
  }
  .contact-line b { font-weight: 700; }
</style>
</head>
<body>

<section class="page page--front">
  <div class="brand-wordmark">Walbert</div>

  <div class="photo front-photo" role="img" aria-label="Foto: Hand hält eine Flasche Schwäbischer Dry Gin mit Porträtetikett vor See im Abendlicht"></div>

  <ul class="hashtags">
    <li>#Ehrlich</li>
    <li>#Traditionell</li>
    <li>#Schwäbisch</li>
    <li>#Einzigartig</li>
  </ul>

  <div class="text-panel">
    <p class="panel-copy">
      <b>WALBERT</b> - ein einzigartig erfrischender GIN, den wir als Hommage<br>
      an unseren lieben <i>Großvater Walbert</i> nach alter Tradition in seiner<br>
      Brennerei herstellen.<br>
      Unser original handcrafted <b>WalbertGIN</b> wird über eine<br>
      Woche mit 13 ausgewählten, feinst aufeinander<br>
      abgestimmten Botanicals in 4-fach gefiltertem<br>
      Kornbrand mazeriert und anschließend gebrannt.<br>
      Er&nbsp; zeichnet sich so durch sein besonderes, zitrus-<br>
      frisches und vollmundiges Aroma, aus und macht<br>
      unseren <b>WalbertGIN</b> zu einem einzigartig fruchtigen Geschmacks-<br>
      erlebnis! Muss man probiert haben!
    </p>
    <div class="photo panel-photo grandfather-photo" role="img" aria-label="Foto: Großvater sitzt lächelnd auf einem Traktor vor einer Obstwiese"></div>
  </div>

  <p class="product-caption">Unser Klassiker: der Walbert „Schwäbischer Dry Gin“</p>
  <p class="label-note">
    Die Etiketten für unseren <b>WalbertGIN</b> sind 100% aus <b>Gras nachhaltig und umwelt-</b><br>
    <b>schonend</b> hergestellt Auch hier achten wir ganz genau auf das Detail für Qualität<br>
    und bewussten Umgang mit der Natur. Außerdem sieht es so besser aus.&nbsp; ;-)
  </p>

  <p class="web-address">www.walbertsud.com</p>
</section>

<section class="page page--back">
  <div class="photo back-photo" role="img" aria-label="Foto: dunkle Flasche Schwäbischer Dry Gin mit goldenem Verschluss in einem alten Brennereikeller"></div>

  <h2 class="headline">Aus Familientradition<br>besonders edle Tropfen<br>für Genießer</h2>

  <div class="text-panel">
    <p class="panel-copy">
      Wir von <b>WalbertGIN,</b> <i>Lena und Jonas</i>, haben beschlossen, die Tradition<br>
      unseres Großvaters <i>Walbert</i> fortzuführen und das Projekt <b>WalbertGIN</b><br>
      gestartet. Unser Großvater hat uns das Handwerk<br>
      des Schnapsbrennens gelehrt und vererbt. Jetzt<br>
      geben wir alles dafür, in seinem Sinne <i>ehrliche</i><br>
      <i>Qualität und höchsten Geschmack</i> mit unserem<br>
      <b>WalbertGIN</b> zu erzielen.<br>
      Eines der Geheimnisse für den außergewöhnlichen<br>
      Geschmack des <b>WalbertGIN</b> sind die 13 speziell aus-<br>
      gewählten und aufeinander fein abgestimmten<br>
      „Botanicals“. Und viel Liebe und Leidenschaft.<br>
      … man schmeckt's.
    </p>
    <div class="photo panel-photo founders-photo" role="img" aria-label="Foto: zwei Gründer in T-Shirts an einem Tisch im Hof beim Abfüllen"></div>
    <div class="brand-signoff"><span class="dot"></span>Walbert GIN</div>
  </div>

  <p class="web-address">www.walbertsud.com</p>
  <p class="contact-line"><b>WalbertGIN</b> . Lindenweg 4 . Oberau . 71234 Talheim . +49 151 2384709 . hallo@walbertsud.com</p>
</section>

</body>
</html>
```